Looking for a modern website banner design

Bramblecrest Coaching Partners looking for the development of the main banner of the website. The project description and photos are included in the upload files.

```html
<!DOCTYPE html>
<html lang="en">
<head>
<meta charset="utf-8">
<title>Bramblecrest Coaching Partners — Home Banner</title>
<link href="https://fonts.googleapis.com/css2?family=Archivo:wght@400;800&family=Yellowtail&display=swap" rel="stylesheet">
<style>
  :root {
    --ink: #000000;
    --paper: #ffffff;
    --accent-blue: #1d6fc4;
    --muted: #d9d9d9;
    --photo-dark: #1a1c24;
    --photo-red: #b3141c;
  }
  * { margin: 0; padding: 0; box-sizing: border-box; }
  html, body {
    width: 1200px; height: 562px; overflow: hidden; background: var(--ink);
  }
  .banner {
    position: relative; width: 1200px; height: 562px; background: var(--ink);
    font-family: "Archivo", Arial, sans-serif; color: var(--paper);
  }
  .intro {
    position: absolute; left: 0; top: 0; width: 638px; height: 562px;
  }
  .brand {
    position: absolute; top: 44px; left: 0; width: 638px;
    display: flex; justify-content: center; align-items: center; gap: 12px;
  }
  .brand-dot {
    width: 30px; height: 30px; border-radius: 50%; background: var(--accent-blue);
  }
  .brand-name {
    font-weight: 800; font-size: 22px; letter-spacing: 0.5px; color: var(--paper);
  }
  .testimonial {
    position: absolute; top: 145px; left: 0; width: 638px;
    text-align: center; font-weight: 800; font-size: 15.6px;
    line-height: 18.9px; letter-spacing: 0.4px; text-transform: uppercase;
  }
  .testimonial sup { font-size: 9px; vertical-align: 6px; }
  .signature {
    position: absolute; top: 296px; left: 96px; width: 445px;
    display: flex; align-items: center; justify-content: space-between;
  }
  .signature-rule { width: 76px; height: 2px; background: var(--paper); }
  .signature-name {
    font-family: "Yellowtail", cursive; font-size: 60px; line-height: 1;
    white-space: nowrap;
  }
  .credit {
    position: absolute; left: 0; width: 638px; text-align: center;
    font-weight: 800; font-size: 15.5px; letter-spacing: 0.6px; text-transform: uppercase;
  }
  .credit-team { top: 367px; }
  .credit-league { top: 393px; }
  .cta {
    position: absolute; top: 481px; left: 166px; width: 189px; height: 55px;
    border: 2px solid var(--accent-blue);
    display: flex; align-items: center; justify-content: center;
    font-weight: 800; font-size: 12.5px; letter-spacing: 0.4px; color: var(--paper);
    text-decoration: none; text-transform: uppercase;
  }
  .scroll-hint {
    position: absolute; top: 500px; left: 368px;
    font-weight: 400; font-size: 10.5px; color: var(--muted);
  }
  .hero-photo {
    position: absolute; top: 0; left: 638px; width: 562px; height: 562px;
    background:
      radial-gradient(ellipse at 78% 35%, rgba(179,20,28,0.85) 0%, rgba(179,20,28,0) 55%),
      radial-gradient(ellipse at 50% 80%, #2b3040 0%, rgba(43,48,64,0) 60%),
      linear-gradient(160deg, #2a2a30 0%, var(--photo-dark) 45%, #3a1216 100%);
  }
</style>
</head>
<body>
  <section class="banner">
    <div class="intro">
      <div class="brand">
        <span class="brand-dot"></span>
        <span class="brand-name">Bramblecrest Coaching Partners</span>
      </div>

      <blockquote class="testimonial">
        "Bramblecrest has provided support that has<br>
        allowed me to develop as a<br>
        person and an athlete.<br>
        The S.T.R.I.D.E<sup>TM</sup> process allowed me to<br>
        stay focused on attainable goals<br>
        each season and progress from<br>
        from junior to college and now professional hockey."
      </blockquote>

      <div class="signature">
        <span class="signature-rule"></span>
        <span class="signature-name">Marcus Delorme</span>
        <span class="signature-rule"></span>
      </div>

      <p class="credit credit-team">Lakeshore Tempest</p>
      <p class="credit credit-league">Northern Shore Hockey League</p>

      <a class="cta" href="#">Try Bramblecrest</a>
      <span class="scroll-hint">or Scroll for more info</span>
    </div>

    <div class="hero-photo" role="img" aria-label="Photo of a smiling hockey player in a dark and red jersey walking out of the tunnel, high-fiving young fans in team jerseys leaning over the railing"></div>
  </section>
</body>
</html>
```